Innovative Funky Australian Start Up - HR & Recruitment

We would like a brochure for our company "Crew Harbor". We provide affordable HR & Recruitment support for Small to Medium businesses.
We like a simple, fresh, crisp, clean look. Nothing overly complicated.
Target market is Small and medium businesses with 2-50 employees, this could be in IT, Accounting, Construction, Marketing or a Engineering, so really trying to appeal to all industries. We don’t want to come across as too high end corporate – more everyday professional. I’d say our target client is probably late 30’s to late 40’s owner or general manager
Our website is - www.crewharbor-example.com.au

Target Market(s)

Small and medium size business's.
Business owners.
Multiple industries

Industry/Entity Type

It Company

Font styles to use
Sans Serif

```html
<!DOCTYPE html>
<html lang="en">
<head>
<meta charset="utf-8">
<title>Crew Harbor – Your HR Team Brochure</title>
<link rel="stylesheet" href="https://fonts.googleapis.com/css2?family=Lato:wght@400;700&family=Marcellus&display=swap">
<style>
  :root {
    --backdrop: #4a3427;
    --page-top: #f3f3f3;
    --page-bottom: #ffffff;
    --ink: #2f3b48;
    --brand-yellow: #f5b01a;
    --soft-yellow: #f8d581;
    --link-blue: #1a5fa8;
    --navy: #1e2a78;
    --accent-blue: #2f7fd6;
    --accent-cyan: #2bb8dc;
    --accent-orange: #ee8a22;
    --brand-square: #1d5fb8;
    --photo-warm: #c9a37d;
    --photo-deep: #6d5140;
  }
  * { margin: 0; padding: 0; box-sizing: border-box; }
  html, body { width: 1200px; height: 848px; overflow: hidden; }
  body { background: var(--backdrop); position: relative; font-family: "Lato", Arial, sans-serif; }

  .page {
    position: absolute;
    background: linear-gradient(180deg, var(--page-top), var(--page-bottom) 60%, var(--page-top));
    box-shadow: 0 2px 6px rgba(0,0,0,.35);
    overflow: hidden;
  }
  .page--front { left: 48px; top: 49px; width: 537px; height: 753px; }
  .page--back  { left: 618px; top: 47px; width: 540px; height: 757px; }

  .brand { position: absolute; display: flex; align-items: center; gap: 14px; }
  .brand__square { background: var(--brand-square); }
  .brand__name { font-family: "Lato", Arial, sans-serif; font-weight: 700; color: var(--ink); letter-spacing: -0.5px; white-space: nowrap; }

  .page--front .brand { left: 128px; top: 48px; }
  .page--front .brand__square { width: 50px; height: 50px; }
  .page--front .brand__name { font-size: 36px; }

  .hero { position: absolute; left: 0; top: 107px; width: 537px; height: 444px; }
  .hero__photo {
    position: absolute; inset: 0;
    background: linear-gradient(120deg, #b79474 0%, var(--photo-warm) 35%, #e5d6c4 55%, #4f6a5e 75%, var(--photo-deep) 100%);
  }
  .hero__chevron { position: absolute; left: 0; top: 0; }

  .title-band {
    position: absolute; left: 0; top: 551px; width: 537px; height: 72px;
    background: var(--brand-yellow);
    display: flex; align-items: center; justify-content: center;
  }
  .title-band h1 { font-family: "Marcellus", Georgia, serif; font-weight: 400; font-size: 50px; color: #1c1a16; letter-spacing: 1px; }

  .front-url {
    position: absolute; left: 0; width: 537px; top: 645px; text-align: center;
    font-family: "Marcellus", Georgia, serif; font-size: 18px; color: var(--link-blue);
  }

  .footer-accent {
    position: absolute; bottom: 0;
    background: linear-gradient(90deg, var(--accent-blue), var(--accent-cyan) 50%, var(--accent-orange));
    opacity: .9;
  }
  .page--front .footer-accent { left: 194px; width: 162px; height: 10px; }
  .page--back .footer-accent { left: 216px; width: 130px; height: 8px; }

  .page--back .brand { left: 150px; top: 255px; }
  .page--back .brand__square { width: 46px; height: 46px; }
  .page--back .brand__name { font-size: 32px; }

  .contact-box {
    position: absolute; left: 124px; top: 343px; width: 293px; height: 123px;
    border: 2px solid #2a2d33; border-radius: 6px; background: #fff;
  }
  .contact-box h2 {
    font-family: "Lato", Arial, sans-serif; font-weight: 400; font-size: 18px;
    color: var(--navy); text-align: center; letter-spacing: 1px; margin-top: 6px;
  }
  .contact-box__intro {
    margin: 5px auto 0; width: 225px; background: var(--soft-yellow);
    font-size: 11px; font-weight: 700; color: #2b2b2b; text-align: center; line-height: 13px; padding: 3px 2px;
  }
  .contact-box__list { list-style: none; margin: 7px 0 0 70px; font-size: 10.5px; color: #1f1f1f; line-height: 15px; }
  .contact-box__list b { color: var(--navy); }
</style>
</head>
<body>

<section class="page page--front">
  <div class="brand">
    <span class="brand__square"></span>
    <span class="brand__name">Crew Harbor</span>
  </div>

  <div class="hero">
    <div class="hero__photo" role="img" aria-label="Photo of a smiling café owner in a checked shirt standing beside an espresso machine"></div>
    <svg class="hero__chevron" width="537" height="444" viewBox="0 0 537 444" aria-hidden="true">
      <polygon points="0,-1 537,-1 537,0 324,79 0,0" fill="#f6f6f6"/>
    </svg>
  </div>

  <div class="title-band"><h1>Your HR Team</h1></div>

  <p class="front-url">www.crewharbor-example.com.au</p>

  <div class="footer-accent" role="img" aria-label="Decorative colour accent in blue, cyan and orange"></div>
</section>

<section class="page page--back">
  <div class="brand">
    <span class="brand__square"></span>
    <span class="brand__name">Crew Harbor</span>
  </div>

  <div class="contact-box">
    <h2>CONTACT US:</h2>
    <p class="contact-box__intro">Please contact us to discuss how Crew Harbor can assist your organisation.</p>
    <ul class="contact-box__list">
      <li><b>Email:</b> info@crewharbor-example.com.au</li>
      <li><b>CALL:</b> 1300 000 555</li>
      <li>www.crewharbor-example.com.au</li>
    </ul>
  </div>

  <div class="footer-accent" role="img" aria-label="Decorative colour accent in blue, cyan and orange"></div>
</section>

</body>
</html>
```